Business Card Design for a Lending Business (Hard Money loans)

We need a business card for our Real Estate Lending business. We do hard Money loans for real estate investors. We have an existing logo we like, see attached. I'd like the business card to mostly include the logo colors, but a bright color pop of some sort would be nice to see also. Card should include Logo, Company Name, Company Address, Employee Name, Cell Phone, Main Phone, Email, Website

Industry/Entity Type

Finance / Lending

Contact Information for Business Card

Logo, Company Name, Company Address, Employee Name, Cell Phone, Main Phone, Email, Website

Requirements
Nice to have
• I'd like the business card to mostly include the logo colors, but a bright color pop of some sort would be nice to see also.

```html
<!DOCTYPE html>
<html lang="en">
<head>
<meta charset="utf-8">
<title>Crestline Lending – Business Card</title>
<link href="https://fonts.googleapis.com/css2?family=Montserrat:wght@400;500;600;700&display=swap" rel="stylesheet">
<style>
  :root {
    --navy: #0b2d8f;
    --sky: #1aa6e0;
    --backdrop: #dde1e4;
    --card: #ffffff;
    --ghost: #edf0f6;
  }
  * { box-sizing: border-box; margin: 0; padding: 0; }
  html, body { width: 1200px; height: 1000px; overflow: hidden; }
  body {
    background: var(--backdrop);
    font-family: "Montserrat", sans-serif;
    color: var(--navy);
    position: relative;
  }
  .card {
    position: absolute;
    left: 279px;
    width: 628px;
    height: 377px;
    background: var(--card);
    overflow: hidden;
  }
  .card--front { top: 80px; }
  .card--back { top: 537px; }

  .brand {
    position: absolute;
    display: flex;
    flex-direction: column;
    align-items: center;
    color: var(--navy);
    font-weight: 600;
    text-transform: uppercase;
    line-height: 1;
  }
  .brand__dot { border-radius: 50%; background: var(--sky); }
  .brand__name { letter-spacing: 0.08em; }
  .brand__sub { letter-spacing: 0.3em; }

  .card--front .brand { left: 0; right: 0; top: 112px; }
  .card--front .brand__dot { width: 74px; height: 74px; margin-bottom: 28px; }
  .card--front .brand__name { font-size: 34px; }
  .card--front .brand__sub { font-size: 15px; margin-top: 10px; }

  .backdrop-shape {
    position: absolute;
    left: 195px;
    top: 20px;
    width: 420px;
    height: 420px;
    border-radius: 50%;
    background: var(--ghost);
  }

  .card--back .brand { left: 385px; width: 190px; top: 172px; }
  .card--back .brand__dot { width: 58px; height: 58px; margin-bottom: 22px; }
  .card--back .brand__name { font-size: 26px; }
  .card--back .brand__sub { font-size: 12px; margin-top: 8px; }

  .person { position: absolute; left: 69px; top: 68px; }
  .person__name { font-size: 25px; font-weight: 400; letter-spacing: 0.02em; }
  .person__name strong { font-weight: 700; }
  .person__role { font-size: 14px; font-weight: 500; margin-top: 2px; }
  .person__rule { width: 170px; height: 2px; background: var(--sky); margin-top: 6px; }

  .contacts { position: absolute; left: 67px; top: 221px; list-style: none; }
  .contacts li {
    display: flex; align-items: center; gap: 10px;
    height: 28px; font-size: 13px; font-weight: 600;
  }
  .contacts svg { width: 25px; height: 25px; flex: none; }
</style>
</head>
<body>
  <section class="card card--front">
    <div class="brand">
      <span class="brand__dot"></span>
      <span class="brand__name">Crestline</span>
      <span class="brand__sub">Lending</span>
    </div>
  </section>

  <section class="card card--back">
    <div class="backdrop-shape" aria-hidden="true"></div>

    <div class="person">
      <p class="person__name">YOUR <strong>NAME</strong></p>
      <p class="person__role">Position Name</p>
      <div class="person__rule"></div>
    </div>

    <ul class="contacts">
      <li>
        <svg viewBox="0 0 26 26" fill="none" stroke="#1aa6e0" stroke-width="1.6"><circle cx="13" cy="13" r="11.5"/><path d="M13 19.5s-4.5-4.6-4.5-7.8a4.5 4.5 0 0 1 9 0c0 3.2-4.5 7.8-4.5 7.8z"/><circle cx="13" cy="11.6" r="1.6"/></svg>
        123 Dummy, Lorem Ipsum
      </li>
      <li>
        <svg viewBox="0 0 26 26" fill="none" stroke="#1aa6e0" stroke-width="1.6"><circle cx="13" cy="13" r="11.5"/><path d="M9.5 8c-.8.5-1.2 1.4-.9 2.4.9 3 3.3 5.5 6.3 6.5 1 .3 2 0 2.5-.9l.4-.7-2.3-1.6-1.1 1c-1.4-.7-2.5-1.8-3.2-3.2l1-1.1L10.7 8z" fill="#1aa6e0" stroke="none"/></svg>
        +00 1234 5XXX 9012
      </li>
      <li>
        <svg viewBox="0 0 26 26" fill="none" stroke="#1aa6e0" stroke-width="1.6"><circle cx="13" cy="13" r="11.5"/><rect x="7.5" y="9" width="11" height="8" rx="1" fill="#1aa6e0" stroke="none"/><path d="M7.8 9.5l5.2 4 5.2-4" stroke="#fff" stroke-width="1.2"/></svg>
        your email space
      </li>
      <li>
        <svg viewBox="0 0 26 26" fill="none" stroke="#1aa6e0" stroke-width="1.6"><circle cx="13" cy="13" r="11.5"/><path d="M10 7.5l0 10.5 2.6-2.5 1.8 3.8 1.6-.8-1.8-3.7 3.6-.2z" fill="#1aa6e0" stroke="none"/></svg>
        website address here
      </li>
    </ul>

    <div class="brand">
      <span class="brand__dot"></span>
      <span class="brand__name">Crestline</span>
      <span class="brand__sub">Lending</span>
    </div>
  </section>
</body>
</html>
```